Design für Auto-Folierung, Lieferwagen Tischlerei

Design für Lieferwagen Valbrand Kurier mit Kofferaufbau.
(Valbrand Kurier 428TXL Koffer 4325 Farbe weiß, Baujahr 2020)
Es sollte vom Design zu Holz, Möbel, Tischler, Firmenlogo passen.
Farben sollten zum Firmenlogo und der Wagenfarbe passen.
Es sollte modern und zeitlos sein.
Zusätzlicher Text und Bilder können verwendet werden.
Es würde vermutlich reichen den Aufbau und Motorhaube zu folieren, bin aber für alles offen.
Integriert werden sollte: Firmenlogo (rundum) und Anschrift (hinten) .

• Logo, Anschrift

```html
<!DOCTYPE html>
<html lang="de">
<head>
<meta charset="utf-8">
<title>HOLM Tischlerei – Fahrzeugfolierung</title>
<link href="https://fonts.googleapis.com/css2?family=Michroma&family=Oswald:wght@600&family=Poppins:wght@500;600&display=swap" rel="stylesheet">
<style>
  :root{
    --navy:#141a4a;
    --gold:#c9a548;
    --gold-light:#e2c777;
    --white:#ffffff;
    --panel:#f7f7f7;
    --wood-dark:#8a6440;
    --wood-light:#d9c3a3;
    --bg:#ffffff;
  }
  html,body{margin:0;padding:0;overflow:hidden;}
  body{width:1200px;height:1200px;background:var(--bg);}
  .wrap-layout{display:block;width:1200px;height:1200px;}
  .brand-name{font-family:"Michroma",sans-serif;fill:var(--navy);}
  .brand-sub{font-family:"Michroma",sans-serif;fill:var(--gold);}
  .service-list{font-family:"Oswald",sans-serif;font-weight:600;fill:var(--navy);letter-spacing:.3px;}
  .phone{font-family:"Poppins",sans-serif;font-weight:600;fill:var(--gold-light);}
  .web{font-family:"Poppins",sans-serif;font-weight:500;fill:var(--white);}
  .web-tld{fill:var(--gold-light);}
</style>
</head>
<body>
<svg class="wrap-layout" viewBox="0 0 1200 1200" xmlns="http://www.w3.org/2000/svg">
  <defs>
    <linearGradient id="woodPhoto" x1="0" y1="0" x2="0" y2="1">
      <stop offset="0" stop-color="#a07a52"/>
      <stop offset=".45" stop-color="#cdb48f"/>
      <stop offset="1" stop-color="var(--wood-dark)"/>
    </linearGradient>
    <linearGradient id="goldBand" x1="0" y1="0" x2="1" y2="0">
      <stop offset="0" stop-color="#b8903a"/>
      <stop offset=".5" stop-color="#e6cc84"/>
      <stop offset="1" stop-color="#b8903a"/>
    </linearGradient>
  </defs>

  <!-- Koffer-Seitenfläche -->
  <g class="box-panel" transform="translate(50,396)">
    <rect class="box-base" x="0" y="0" width="800" height="408" fill="var(--panel)"/>
    <polygon class="interior-photo" role="img" aria-label="Foto eines hellen Essbereichs mit Holztisch, Stühlen und Eckbank vor großem Fenster" points="0,0 206,0 357,408 0,408" fill="url(#woodPhoto)"/>
    <polygon class="diagonal-edge" points="206,0 222,0 373,408 357,408" fill="var(--navy)"/>
    <polygon class="navy-band" points="318,282 800,282 800,408 365,408" fill="var(--navy)"/>
    <polygon class="gold-band" points="308,256 800,256 800,282 318,282" fill="url(#goldBand)"/>
    <text class="service-list" x="335" y="275" font-size="14.5">KÜCHE • ESSZIMMER • WOHNZIMMER • SCHLAFZIMMER • BAD • VERSCHIEDENES</text>

    <rect class="brand-square" x="340" y="86" width="100" height="100" fill="var(--gold)"/>
    <text class="brand-name" x="470" y="158" font-size="74">HOLM</text>
    <text class="brand-sub" x="474" y="198" font-size="27">TISCHLEREI</text>

    <text class="phone" x="408" y="345" font-size="36">+43 660 5813274</text>
    <text class="web" x="408" y="380" font-size="27">www.holm-tischlerei<tspan class="web-tld">.at</tspan></text>
  </g>

  <!-- Fahrerhaus-Seitenfläche -->
  <g class="cab-panel" transform="translate(866,396)">
    <path class="cab-base" d="M0,0 H170 Q230,60 270,170 Q290,200 290,240 V408 H0 Z" fill="var(--white)" stroke="#d6d6d6"/>
    <polygon class="cab-gold" points="0,256 250,256 262,282 0,282" fill="url(#goldBand)"/>
    <path class="cab-navy" d="M0,282 H262 Q290,300 290,330 V408 H0 Z" fill="var(--navy)"/>
    <g class="social-dots" fill="var(--white)">
      <circle cx="80" cy="356" r="9"/>
      <circle cx="108" cy="356" r="9"/>
      <circle cx="136" cy="356" r="9"/>
      <circle cx="164" cy="356" r="9"/>
    </g>
  </g>
</svg>
</body>
</html>
```